Corbel Insurance Agency, Inc.
www.corbelinsagy.example
Project: Corbel Insurance Agency, Inc.
Corbel Insurance Agency, Inc. -
Creative Brief
Independent insurance agency created in 1938.
Like: Simple design and easy to use.
Service Oriented
Arial, Verdana, Times New Roman
left side
http://www.tallisinsagency.example/
http://pruett-insurance.example/

```html
<!DOCTYPE html>
<html lang="en">
<head>
<meta charset="utf-8">
<title>Corbel Insurance Agency, Inc.</title>
<link rel="stylesheet" href="https://fonts.googleapis.com/css2?family=Arimo:wght@400;700&display=swap">
<style>
:root{
  --page:#e4e4f1;
  --page-line:#dcdcec;
  --ink:#333;
  --muted:#777;
  --navy:#1c2c52;
  --blue:#1a6fb5;
  --link:#1f5fa8;
  --orange:#e07a12;
  --bar:#262626;
  --bar-edge:#3b3b3b;
  --white:#fff;
  --footer:#1f1f22;
  --footer-text:#9a9aa0;
}
*{box-sizing:border-box;margin:0;padding:0}
html,body{width:1200px;height:1052px;overflow:hidden}
body{
  font-family:"Arimo",Arial,sans-serif;color:var(--ink);
  background:var(--page) repeating-linear-gradient(45deg,transparent 0 6px,var(--page-line) 6px 7px);
  position:relative;
}
.brand{position:absolute;left:108px;top:62px;width:480px}
.brand-name{display:flex;align-items:center;gap:10px;font-size:24px;font-weight:700;color:var(--navy);line-height:1.1;white-space:nowrap}
.brand-mark{width:22px;height:22px;background:var(--navy);flex:none}
.brand-tagline{margin-top:14px;display:inline-block;background:#111;color:#fff;font-size:11px;padding:3px 8px;white-space:nowrap}
.hotline{position:absolute;right:120px;top:40px;text-align:right}
.hotline-title{font-size:24px;font-weight:700;color:var(--blue);font-style:italic}
.hotline-number{font-size:24px;color:var(--orange);margin-top:6px;display:flex;align-items:center;gap:8px;justify-content:flex-end}
.search{position:absolute;left:847px;top:128px;width:233px;height:30px;display:flex}
.search-field{flex:1;background:#2d3340;color:#aab;font-size:13px;padding:7px 10px}
.search-btn{width:34px;background:var(--blue);display:flex;align-items:center;justify-content:center}
.nav{position:absolute;left:108px;top:190px;width:972px;height:52px;background:var(--bar);border-top:2px solid var(--bar-edge);display:flex;align-items:center;padding-left:10px}
.nav a{color:var(--white);text-decoration:none;font-size:16px;padding:0 19px;white-space:nowrap}
.hero{position:absolute;left:108px;top:264px;width:972px;height:304px;background:var(--white);border:1px solid #d4d4e0;display:flex}
.hero-text{width:490px;padding:22px 24px;flex:none}
.hero-title{font-size:23px;color:var(--blue);font-weight:700;line-height:1.3;letter-spacing:.3px}
.hero-copy{margin-top:18px;font-size:13px;color:var(--muted);line-height:1.75}
.btn-more{margin-top:22px;margin-left:320px;display:inline-flex;align-items:center;gap:8px;background:#eee;border:1px solid #ccc;padding:6px 10px;font-weight:700;font-size:15px;color:#222;white-space:nowrap}
.hero-visual{flex:1;background:radial-gradient(circle at 62% 48%,#e9a3a3 0,#f3d3d3 30%,#f7f7f7 62%)}
.features{position:absolute;left:108px;top:603px;width:972px;display:flex;gap:26px}
.feature{flex:1;display:flex;gap:12px}
.feature-icon{flex:none;width:28px;height:28px}
.feature h3{font-size:13px;font-weight:700;color:#333;line-height:1.35}
.feature p{margin-top:8px;font-size:11px;color:var(--muted);line-height:1.6}
.feature a{color:var(--link);text-decoration:none}
.cards{position:absolute;left:108px;top:782px;width:972px;display:flex;gap:40px}
.card{flex:1;display:flex;gap:14px}
.card-thumb{width:100px;height:92px;flex:none;margin-top:28px;border:1px solid #bbb}
.card h4{font-size:17px;font-weight:400;color:#333;margin-bottom:8px}
.card p{font-size:11px;color:var(--muted);line-height:1.6}
.footer{position:absolute;left:108px;top:938px;width:972px;height:114px;background:var(--footer)}
.footer-links{position:absolute;right:16px;top:14px;display:flex;gap:22px;font-size:12px;color:var(--footer-text)}
.footer-rule{position:absolute;left:0;right:0;top:40px;border-top:1px solid #333}
.footer-copy{position:absolute;left:10px;top:55px;font-size:12px;color:var(--footer-text);line-height:1.6}
</style>
</head>
<body>
<header>
  <div class="brand">
    <div class="brand-name"><span class="brand-mark"></span>Corbel Insurance Agency, Inc.</div>
    <div class="brand-tagline">Protection for all your insurance needs</div>
  </div>
  <div class="hotline">
    <div class="hotline-title">24/7 Support Hotline!</div>
    <div class="hotline-number">
      <svg width="20" height="20" viewBox="0 0 20 20"><path d="M5 2l3 4-2 2a10 10 0 006 6l2-2 4 3-2 3C9 18 2 11 2 4z" fill="var(--orange)"/></svg>
      1234-5550-0100-1
    </div>
  </div>
  <div class="search">
    <div class="search-field">Search</div>
    <div class="search-btn"><svg width="14" height="12" viewBox="0 0 14 12"><rect x="1" y="1" width="12" height="10" fill="none" stroke="#fff" stroke-width="1.5"/><path d="M1 1l6 5 6-5" fill="none" stroke="#fff" stroke-width="1.5"/></svg></div>
  </div>
</header>

<nav class="nav">
  <a>HOME</a><a>PARTNERS</a><a>DIRECTORY</a><a>EVENTS</a><a>TECHNCAL ISSUES</a><a>INSURANCES</a><a>CONTACT US</a>
</nav>

<section class="hero">
  <div class="hero-text">
    <h1 class="hero-title">We Provide The Best Services In The Insurance Industry.</h1>
    <p class="hero-copy">An adjunct analgesic for neuropathic pain. It is a synthetic cannabinoid, which mimics the main ingredient of marijuana (THC).an adjunct analgesic for neuropathic pain. It is a synthetic cannabinoid, which mimics the main ingredient of marijuana (THC).An adjunct analgesic for neuropathic pain. It is a synthetic cannabinoid, which mimics the main ingredient of marijuana (THC).an adjunct analgesic for neuropathic pain.</p>
    <div class="btn-more">Learn More
      <svg width="18" height="18" viewBox="0 0 18 18"><path d="M7 1h4v6h6v4h-6v6H7v-6H1V7h6z" fill="#5aa02c"/></svg>
    </div>
  </div>
  <div class="hero-visual" role="img" aria-label="Red and white target with a dart in the bullseye"></div>
</section>

<section class="features">
  <div class="feature">
    <svg class="feature-icon" viewBox="0 0 28 28"><circle cx="14" cy="14" r="12" fill="#3a9fd8"/><path d="M2 14h24M14 2c-5 6-5 18 0 24M14 2c5 6 5 18 0 24" stroke="#fff" fill="none"/></svg>
    <div><h3>Lorem Ipsum is simply dummy text of the printing</h3>
    <p>Lorem Ipsum is simply dummy text of the printing and typesetting industry. Lorem Ipsum has been the industry's standard dummy text.<br>Lorem Ipsum is simply dummy text of the printing and typesetting. <a>continue reading »</a></p></div>
  </div>
  <div class="feature">
    <svg class="feature-icon" viewBox="0 0 28 28"><rect x="3" y="9" width="22" height="15" rx="2" fill="#c98a2a"/><rect x="10" y="5" width="8" height="5" fill="none" stroke="#8a5a14" stroke-width="2"/></svg>
    <div><h3>Lorem Ipsum is simply dummy text of the printing</h3>
    <p>Lorem Ipsum is simply dummy text of the printing and typesetting industry. Lorem Ipsum has been the industry's standard dummy text.<br>Lorem Ipsum is simply dummy text of the printing and typesetting. <a>continue reading »</a></p></div>
  </div>
  <div class="feature">
    <svg class="feature-icon" viewBox="0 0 28 28"><rect x="2" y="2" width="24" height="24" rx="5" fill="#f08a1c"/><circle cx="9" cy="19" r="2" fill="#fff"/><path d="M7 12a9 9 0 019 9M7 7a14 14 0 0114 14" stroke="#fff" stroke-width="2.5" fill="none"/></svg>
    <div><h3>Lorem Ipsum is simply dummy text of the printing</h3>
    <p>Lorem Ipsum is simply dummy text of the printing and typesetting industry. Lorem Ipsum has been the industry's standard dummy text.<br>Lorem Ipsum is simply dummy text of the printing and typesetting. <a>continue reading »</a></p></div>
  </div>
</section>

<section class="cards">
  <div class="card">
    <div class="card-thumb" role="img" aria-label="Blue financial chart with pen" style="background:linear-gradient(135deg,#2f5f9e,#9fc1e6)"></div>
    <div><h4>Featured Products</h4><p>Lorem Ipsum is simply dummy text of the printing and typesetting industry. Lorem Ipsum has been the industry's standard text</p></div>
  </div>
  <div class="card">
    <div class="card-thumb" role="img" aria-label="Fountain pen resting on a signed document" style="background:linear-gradient(135deg,#f4f4f4,#b9b9b9)"></div>
    <div><h4>Our Services</h4><p>Lorem Ipsum is simply dummy text of the printing and typesetting industry. Lorem Ipsum has been the industry's standard text</p></div>
  </div>
  <div class="card">
    <div class="card-thumb" role="img" aria-label="Metallic percent symbol" style="background:linear-gradient(135deg,#eaeaea,#9a9a9a)"></div>
    <div><h4>Our Speciality</h4><p>Lorem Ipsum is simply dummy text of the printing and typesetting industry. Lorem Ipsum has been the industry's standard text</p></div>
  </div>
</section>

<footer class="footer">
  <div class="footer-links"><span>Our Services</span><span>Services List</span><span>Online Support</span><span>Sitemap</span></div>
  <div class="footer-rule"></div>
  <div class="footer-copy">Site content © 2011 Corbel Insurance Agency<br>All right reserved</div>
</footer>
</body>
</html>
```